Business Card for Brightwave Reach

Please design a Modern Business card for a Online Marketing Company

Website: http://www.brightwavereach.com.au

Please do NOT include physical address in design.

Industry/Entity Type

Business

```html
<!DOCTYPE html>
<html lang="en">
<head>
<meta charset="utf-8">
<title>Brightwave Reach – Business Card</title>
<link href="https://fonts.googleapis.com/css2?family=Roboto+Condensed:wght@400;700&family=Roboto:wght@400;700&display=swap" rel="stylesheet">
<style>
  :root {
    --backdrop: #1c2942;
    --card-white: #ffffff;
    --brand-red: #b8111c;
    --card-red: #c1091a;
    --card-red-soft: #d12a38;
    --ink: #111111;
    --name-pale: #f0b7bc;
    --url-pale: #f3c9cc;
    --seg-1: #ffd23f;
    --seg-2: #ff9f1c;
    --seg-3: #f4f1de;
    --seg-4: #2ec4b6;
    --seg-5: #3a86ff;
    --seg-6: #9b5de5;
    --hub: #ffffff;
    --gap-line: #ffffff;
  }
  * { box-sizing: border-box; margin: 0; padding: 0; }
  html, body {
    width: 1200px;
    height: 779px;
    overflow: hidden;
  }
  body {
    background: var(--backdrop);
    font-family: "Roboto", Arial, sans-serif;
  }
  .canvas {
    position: relative;
    width: 1200px;
    height: 779px;
    display: flex;
    align-items: center;
    justify-content: center;
    gap: 40px;
  }
  .card {
    position: relative;
    width: 540px;
    height: 310px;
    border-radius: 28px;
    overflow: hidden;
  }

  /* Front side */
  .card-front {
    background: var(--card-white);
    display: flex;
    flex-direction: column;
    align-items: center;
    justify-content: center;
    padding-top: 30px;
  }
  .brand-lockup {
    display: flex;
    align-items: center;
    gap: 14px;
  }
  .brand-square {
    width: 30px;
    height: 30px;
    background: var(--brand-red);
  }
  .brand-name {
    font-family: "Roboto Condensed", Arial, sans-serif;
    font-weight: 700;
    font-size: 44px;
    letter-spacing: 0.5px;
    color: var(--brand-red);
    line-height: 1;
  }
  .tagline {
    font-family: "Roboto Condensed", Arial, sans-serif;
    font-weight: 700;
    font-size: 21px;
    color: var(--ink);
    margin-top: 6px;
    margin-left: 44px;
  }
  .website {
    font-size: 15px;
    color: var(--brand-red);
    margin-top: 52px;
  }

  /* Back side */
  .card-back {
    background: var(--card-red);
  }
  .back-panel {
    position: absolute;
    left: 0;
    top: 0;
    width: 540px;
    height: 310px;
  }
  .back-copy {
    position: absolute;
    left: 40px;
    top: 58px;
    width: 240px;
  }
  .back-name {
    font-family: "Roboto Condensed", Arial, sans-serif;
    font-weight: 700;
    font-size: 25px;
    color: var(--name-pale);
    line-height: 1;
  }
  .back-tagline {
    font-family: "Roboto Condensed", Arial, sans-serif;
    font-weight: 700;
    font-size: 13px;
    color: var(--ink);
    margin-top: 3px;
    margin-left: 30px;
  }
  .back-website {
    font-size: 10px;
    color: var(--url-pale);
    margin-top: 6px;
    margin-left: 30px;
  }
  .cycle-chart {
    position: absolute;
    left: 280px;
    top: 35px;
    width: 240px;
    height: 240px;
  }
  .cycle-label {
    font-family: "Roboto", Arial, sans-serif;
    font-size: 10px;
    fill: var(--ink);
    text-anchor: middle;
    dominant-baseline: middle;
  }
</style>
</head>
<body>
  <main class="canvas">
    <section class="card card-front" aria-label="Card front">
      <div class="brand-lockup">
        <span class="brand-square"></span>
        <h1 class="brand-name">BRIGHTWAVE REACH</h1>
      </div>
      <p class="tagline">Be seen online - Grow online</p>
      <p class="website">www.brightwavereach.com.au</p>
    </section>

    <section class="card card-back" aria-label="Card back">
      <svg class="back-panel" viewBox="0 0 540 310" aria-hidden="true">
        <path d="M0 40 Q0 0 40 0 L140 0 Q175 0 195 40 L200 60 Q215 110 180 150 L40 300 Q30 310 15 310 L0 310 Z" fill="var(--card-red-soft)" opacity="0.85"/>
      </svg>

      <div class="back-copy">
        <h2 class="back-name">BRIGHTWAVE REACH</h2>
        <p class="back-tagline">Be seen online - Grow online</p>
        <p class="back-website">www.brightwavereach.com.au</p>
      </div>

      <svg class="cycle-chart" viewBox="-120 -120 240 240" role="img" aria-label="Pie chart: research, review, targets, execute, track, refine">
        <g stroke="var(--gap-line)" stroke-width="2" stroke-linejoin="round">
          <path fill="var(--seg-1)" d="M0 0 L0 -105 A105 105 0 0 1 90.9 -52.5 Z"/>
          <path fill="var(--seg-2)" d="M0 0 L90.9 -52.5 A105 105 0 0 1 90.9 52.5 Z"/>
          <path fill="var(--seg-3)" d="M0 0 L90.9 52.5 A105 105 0 0 1 0 105 Z"/>
          <path fill="var(--seg-4)" d="M0 0 L0 105 A105 105 0 0 1 -90.9 52.5 Z"/>
          <path fill="var(--seg-5)" d="M0 0 L-90.9 52.5 A105 105 0 0 1 -90.9 -52.5 Z"/>
          <path fill="var(--seg-6)" d="M0 0 L-90.9 -52.5 A105 105 0 0 1 0 -105 Z"/>
        </g>
        <circle class="cycle-hub" cx="0" cy="0" r="18" fill="var(--hub)"/>
        <text class="cycle-label" x="36" y="-62">RESEARCH</text>
        <text class="cycle-label" x="66" y="0">REVIEW</text>
        <text class="cycle-label" x="36" y="62">TARGETS</text>
        <text class="cycle-label" x="-36" y="62">EXECUTE</text>
        <text class="cycle-label" x="-64" y="0">TRACK</text>
        <text class="cycle-label" x="-36" y="-62">REFINE</text>
      </svg>
    </section>
  </main>
</body>
</html>
```